Email Signiture and letterhead design

we are looking for a modern business design to incorporate our logo and qel certification plus social icons for Vorlant, Pelmora, and zandoro
they must include our UK vat and also company registration as text but I can fill these out. Email signature to have a link/icon to our webshop www.trexolan.co.uk

Target Market(s)

All

Font styles to use
Serif
Sans Serif

Requirements
Must have
• Address, tel, email , web details incorperated
Nice to have
• a professional looking letter head and email signiture, Email signature to have a link/icon to our webshop www.trexolan.co.uk

```html
<!DOCTYPE html>
<html lang="en">
<head>
<meta charset="utf-8">
<title>Trexolan Hubs &amp; Bearings Ltd — Letterhead and Email Signature</title>
<link href="https://fonts.googleapis.com/css2?family=Questrial&family=Montserrat:wght@700&display=swap" rel="stylesheet">
<style>
  :root{
    --red:#e3141b;
    --ink:#1f1f1f;
    --grey-mark:#3b3b3b;
    --paper:#ffffff;
    --backdrop:#c4c4c4;
    --backdrop-low:#d2d2d2;
    --badge:#f2e6ee;
  }
  *{margin:0;padding:0;box-sizing:border-box}
  html,body{width:1200px;height:1200px;overflow:hidden}
  body{
    position:relative;
    font-family:"Questrial",sans-serif;
    color:var(--ink);
    background:linear-gradient(var(--backdrop) 0 815px,var(--backdrop-low) 815px 100%);
  }

  /* ---------- Letterhead ---------- */
  .letterhead{
    position:absolute;left:44px;top:34px;width:509px;height:768px;
    background:var(--paper);box-shadow:0 2px 8px rgba(0,0,0,.18);
  }
  .letterhead .brand{
    position:absolute;left:0;right:0;top:58px;
    display:flex;justify-content:center;align-items:center;gap:8px;
    font-size:15px;color:var(--red);letter-spacing:.5px;
  }
  .brand-dot{width:12px;height:12px;border-radius:50%;background:var(--red)}
  .letterhead .rule{position:absolute;left:25px;right:20px;top:89px;height:1.5px;background:var(--red)}
  .letterhead .company-address{position:absolute;left:0;right:0;top:98px;text-align:center;font-size:9.5px}
  .letter-date{position:absolute;left:25px;top:162px;font-family:"Montserrat",sans-serif;font-weight:700;font-size:9.5px;letter-spacing:.4px}
  .letter-to{position:absolute;left:25px;top:198px;font-size:9px}
  .recipient{position:absolute;left:25px;top:224px;font-size:8.5px;line-height:15.6px}
  .recipient strong{display:block;font-size:12px;font-weight:700;letter-spacing:.2px;margin-bottom:1px}
  .letter-body{position:absolute;left:25px;right:20px;top:334px;font-size:8.4px;line-height:15.5px}
  .letter-body p{margin-bottom:15.5px;text-align:justify}
  .letter-closing{position:absolute;left:25px;top:565px;font-size:9.5px}
  .signature{position:absolute;left:25px;top:592px;width:112px;height:78px;background:linear-gradient(135deg,#f1f1f1,#e2e2e2);border-radius:4px}
  .cert-badge{position:absolute;left:381px;top:630px;width:96px;height:36px;border:1.5px solid #d6d6d6;border-radius:6px;background:var(--badge);border-right:8px solid #d4167f}
  .cert-number{position:absolute;left:379px;top:669px;font-size:8.5px}
  .letter-footer{
    position:absolute;left:0;right:0;top:726px;height:25px;background:var(--red);
    display:flex;align-items:center;gap:10px;padding-left:22px;color:#fff;font-size:9px;
  }
  .letter-footer span{display:flex;align-items:center;gap:4px}
  .letter-footer svg{width:12px;height:12px}

  /* ---------- Email signature ---------- */
  .signature-card{
    position:absolute;width:987px;height:300px;background:var(--paper);
    box-shadow:0 2px 8px rgba(0,0,0,.18);overflow:hidden;transform-origin:top left;
  }
  .signature-card.compact{left:576px;top:300px;transform:scale(.6)}
  .signature-card.full{left:106px;top:838px}
  .signature-card .tab{position:absolute;left:0;top:112px;width:20px;height:46px;background:var(--red)}
  .signature-card .person{position:absolute;left:49px;top:105px}
  .person .name{font-size:26px;color:var(--red);letter-spacing:.5px;line-height:1.1}
  .person .role{font-size:19px;margin-top:4px}
  .social{position:absolute;left:49px;top:196px;display:flex;gap:10px;font-size:13px;color:var(--red)}
  .social span{border-bottom:1.5px solid var(--red);padding-bottom:1px}
  .divider{position:absolute;top:68px;width:3px;height:149px;background:var(--red)}
  .divider.first{left:275px}
  .divider.second{left:615px}
  .contact{position:absolute;left:317px;top:62px;font-size:19.5px;line-height:28px}
  .contact .lines{margin-top:20px}
  .contact .line{display:flex;align-items:center;gap:6px}
  .contact svg{width:16px;height:16px}
  .contact .web{color:var(--ink)}
  .contact .web b{font-weight:400;color:var(--red)}
  .signature-card .brand{
    position:absolute;left:640px;width:330px;top:148px;
    display:flex;justify-content:center;align-items:center;gap:9px;
    font-size:19px;color:var(--red);letter-spacing:.5px;
  }
  .signature-card .brand-dot{width:15px;height:15px}
  .band-red{position:absolute;left:0;top:255px;width:925px;height:31px;background:var(--red)}
  .band-grey{position:absolute;left:925px;right:0;top:255px;height:31px;background:var(--grey-mark)}
</style>
</head>
<body>

<article class="letterhead">
  <div class="brand"><span class="brand-dot"></span>Trexolan Hubs &amp; Bearings Ltd</div>
  <div class="rule"></div>
  <p class="company-address">14 Harrow Lane, Unit 6, Leeds LS2 7QT</p>

  <p class="letter-date">February, 12, 2021</p>
  <p class="letter-to">To</p>
  <div class="recipient">
    <strong>MR. DARIO FENWICK</strong>
    Founder<br>88 Quarry Row, Ste 12,<br>Brindlehurst, BH4 2RN<br>Post Coad 5400
  </div>

  <div class="letter-body">
    <p>I'm Rafi. I am a student. In this year I passed my Bed Honers. Now I'm try to divlope my life by this freelancer platfrom. I live in Bangladesh. I'm Rafi. I am a student. In this year I passed my Bed rom. I live in Bangladesh.</p>
    <p>I'm Rafi. I am a student. In this year I passed my Bed Honers. Now I'm try to divlope my life by this freelancer platfrom. I live in Bangladesh. I'm Rafi. Now I'm try to divlope my life by this freelancer platfrom. I live in Bangladesh. I'm Rafi. I am a student. In this year I passed my Bed Honers.</p>
    <p>I'm Rafi. I am a student. In this year I passed my Bed Honers. Now I'm try to divlope my life by this freelancer platfrom. I live in Bangladesh. I'm Rafi. Now I'm try to divlope my life by this freelancer platfrom. I live in Bangladesh. I am a student.</p>
    <p>I'm Rafi. I am a student. In this year I passed my Bed Honers. Now I'm try to divlope my life by this freelancer platfrom. I live in Bangladesh. I'm Rafi. Now I'm try to divlope my life by this freelancer platfrom.</p>
  </div>

  <p class="letter-closing">Best Regurd</p>
  <div class="signature" role="img" aria-label="Handwritten signature of Lena Hart"></div>

  <div class="cert-badge" role="img" aria-label="qel quality certification badge"></div>
  <p class="cert-number">Certificat No: 558104273</p>

  <footer class="letter-footer">
    <span><svg viewBox="0 0 16 16"><circle cx="8" cy="8" r="8" fill="#fff"/><path d="M5 4.5h2l.8 2-1.2.8a5 5 0 0 0 2.1 2.1l.8-1.2 2 .8v2c0 .5-.4.8-.9.8A6.3 6.3 0 0 1 4.2 5.4c0-.5.3-.9.8-.9z" fill="#e3141b"/></svg>(555) 014-2280</span>
    <span><svg viewBox="0 0 16 16"><circle cx="8" cy="8" r="8" fill="#fff"/><rect x="4" y="5" width="8" height="6" fill="#e3141b"/><path d="M4 5l4 3.3L12 5" stroke="#fff" fill="none"/></svg>info@trexolan.co.uk</span>
    <span><svg viewBox="0 0 16 16"><circle cx="8" cy="8" r="8" fill="#fff"/><circle cx="8" cy="8" r="4.2" fill="none" stroke="#e3141b" stroke-width="1.2"/><path d="M3.8 8h8.4M8 3.8c-2 2.6-2 5.8 0 8.4M8 3.8c2 2.6 2 5.8 0 8.4" stroke="#e3141b" fill="none"/></svg>www.trexolan.co.uk</span>
  </footer>
</article>

<section class="signature-card compact">
  <div class="tab"></div>
  <div class="person"><p class="name">CORIN VALE</p><p class="role">CEO/ Founder</p></div>
  <div class="social"><span>Vorlant</span><span>Pelmora</span><span>zandoro</span></div>
  <div class="divider first"></div>
  <div class="contact">
    <p>14 Harrow Lane, Unit 6</p><p>Leeds LS2 7QT, UK</p>
    <div class="lines">
      <p class="line"><svg viewBox="0 0 16 16"><path d="M3 3h3l1 3-1.6 1a6.5 6.5 0 0 0 3.6 3.6L10 9l3 1v3c0 .6-.5 1-1 1A11 11 0 0 1 2 4c0-.5.4-1 1-1z" fill="#e3141b"/></svg>(555) 019-4471</p>
      <p class="line"><svg viewBox="0 0 16 16"><rect x="1" y="3.5" width="14" height="9" fill="#e3141b"/><path d="M1 3.5l7 5 7-5" stroke="#fff" fill="none"/></svg>corin@trexolan.co.uk</p>
      <p class="line web"><svg viewBox="0 0 16 16"><circle cx="8" cy="8" r="6.5" fill="#e3141b"/><path d="M1.5 8h13M8 1.5c-3 3.5-3 9.5 0 13M8 1.5c3 3.5 3 9.5 0 13" stroke="#fff" fill="none"/></svg>www.<b>trexolan</b>.co.uk</p>
    </div>
  </div>
  <div class="divider second"></div>
  <div class="brand"><span class="brand-dot"></span>Trexolan Hubs &amp; Bearings Ltd</div>
  <div class="band-red"></div><div class="band-grey"></div>
</section>

<section class="signature-card full">
  <div class="tab"></div>
  <div class="person"><p class="name">CORIN VALE</p><p class="role">CEO/ Founder</p></div>
  <div class="social"><span>Vorlant</span><span>Pelmora</span><span>zandoro</span></div>
  <div class="divider first"></div>
  <div class="contact">
    <p>14 Harrow Lane, Unit 6</p><p>Leeds LS2 7QT, UK</p>
    <div class="lines">
      <p class="line"><svg viewBox="0 0 16 16"><path d="M3 3h3l1 3-1.6 1a6.5 6.5 0 0 0 3.6 3.6L10 9l3 1v3c0 .6-.5 1-1 1A11 11 0 0 1 2 4c0-.5.4-1 1-1z" fill="#e3141b"/></svg>(555) 019-4471</p>
      <p class="line"><svg viewBox="0 0 16 16"><rect x="1" y="3.5" width="14" height="9" fill="#e3141b"/><path d="M1 3.5l7 5 7-5" stroke="#fff" fill="none"/></svg>corin@trexolan.co.uk</p>
      <p class="line web"><svg viewBox="0 0 16 16"><circle cx="8" cy="8" r="6.5" fill="#e3141b"/><path d="M1.5 8h13M8 1.5c-3 3.5-3 9.5 0 13M8 1.5c3 3.5 3 9.5 0 13" stroke="#fff" fill="none"/></svg>www.<b>trexolan</b>.co.uk</p>
    </div>
  </div>
  <div class="divider second"></div>
  <div class="brand"><span class="brand-dot"></span>Trexolan Hubs &amp; Bearings Ltd</div>
  <div class="band-red"></div><div class="band-grey"></div>
</section>

</body>
</html>
```